Design a van wrap

We require a full van wrap design for a construction and development company. The design must present a premium, professional, and highly visible brand image suitable for a modern construction business. See attached existing wrap. Require a whole new look.
Vehicle Details
- Vehicle: Velbro electric van (T7 / similar size)
- Wrap type: Full wrap (bonnet, sides, rear)
- Use Palmet image on the rear doors
Dimension uCarrio 8 L1H1 uCarrio 8 L2H1
Overall length ~4,800 mm ~5,250 mm
Overall width (excl. mirrors) ~1,874 mm ~1,874 mm
Overall height (H1) ~1,960 mm ~1,960 mm
Wheelbase ~3,100 mm ~3,450 mm
Roof height H1 (standard) H1 (standard)
Branding
- Company Name: KORVELT
- Industry: Construction & Development
- 4 bullets on each side of van detailing scope of business
- New Builds
- Basement Works
- Piling Works
- Demolition
- Engineering
- RC Frame Works
- Loft Conversions
- Refurbishment
Brand Style: Modern, strong, premium, clean
- Colours:
- Primary: Black and Brown
- Accent: Cream (for contrast and legibility if required - see business card)
- Existing assets: Logo will be provided (vector format)
Design Style & Finish
- Contemporary and bold
- Strong contrast for roadside visibility
- Suitable for commercial vinyl printing
- Avoid over-complication or excessive textures
Deliverables
- Print-ready files
- Vector format preferred (AI / EPS / PDF)
- High-resolution mockups showing all sides of the van
- Colour codes specified (CMYK / Pantone if applicable)
Target Outcome
A van wrap that clearly communicates professionalism, scale, and trust, stands out on the road, and reinforces a premium construction brand.

```html
<!DOCTYPE html>
<html lang="en">
<head>
<meta charset="utf-8">
<title>KORVELT Van Wrap – Version 6</title>
<link href="https://fonts.googleapis.com/css2?family=Montserrat:wght@700;800&family=Open+Sans:wght@700&display=swap" rel="stylesheet">
<style>
  :root {
    --ink: #0b0b0b;
    --black: #111111;
    --bronze-light: #c9b39a;
    --bronze: #a0836a;
    --bronze-dark: #5e4a3a;
    --cream: #d9c4aa;
    --sand: #cfbda5;
    --white: #ffffff;
    --silver: #e6e6e6;
    --sky: #9fc3e6;
    --brick: #a9583a;
  }
  * { margin: 0; padding: 0; box-sizing: border-box; }
  html, body { width: 1200px; height: 2794px; overflow: hidden; background: var(--white); }
  .canvas { position: relative; width: 1200px; height: 2794px; background: var(--white); }
  .version-title {
    position: absolute; top: 70px; left: 0; width: 1200px; text-align: center;
    font-family: "Open Sans", Arial, sans-serif; font-weight: 700; font-size: 84px;
    letter-spacing: 1px; color: var(--ink);
  }
  .panel { position: absolute; display: block; }
  .side-left  { left: 25px; top: 205px; }
  .side-right { left: 15px; top: 765px; }
  .rear  { left: 265px; top: 1265px; }
  .front { left: 190px; top: 2050px; }
  .brand-name { font-family: "Montserrat", Arial, sans-serif; font-weight: 800; letter-spacing: 6px; }
  .web { font-family: "Montserrat", Arial, sans-serif; font-weight: 800; }
  .phone { font-family: "Montserrat", Arial, sans-serif; font-weight: 800; }
  .service { font-family: "Montserrat", Arial, sans-serif; font-weight: 700; }
</style>
</head>
<body>
<main class="canvas">
  <h1 class="version-title">VERSION - 6</h1>

  <!-- Driver side panel -->
  <svg class="panel side-left" width="1160" height="440" viewBox="0 0 1160 440">
    <defs>
      <linearGradient id="bronzeSide" x1="0" y1="0" x2="0" y2="1">
        <stop offset="0" stop-color="var(--sand)"/>
        <stop offset="0.55" stop-color="var(--bronze)"/>
        <stop offset="1" stop-color="var(--bronze-dark)"/>
      </linearGradient>
      <linearGradient id="buildingTone" x1="0" y1="0" x2="0" y2="1">
        <stop offset="0" stop-color="var(--sky)"/>
        <stop offset="0.3" stop-color="#c98a6a"/>
        <stop offset="0.8" stop-color="var(--brick)"/>
        <stop offset="1" stop-color="#d8d8d8"/>
      </linearGradient>
    </defs>
    <rect class="wrap-base" x="0" y="0" width="1160" height="440" rx="40" fill="url(#bronzeSide)"/>
    <path class="building-photo" role="img" aria-label="Photo of a modern brick apartment building" d="M905 0 H1120 Q1160 0 1160 40 V300 L840 300 C880 210 890 90 905 0 Z" fill="url(#buildingTone)"/>
    <path class="accent-swoosh" d="M905 0 C890 90 880 210 840 300 L1160 300 V318 L380 330 C560 300 760 320 820 290 C860 200 875 90 890 0 Z" fill="var(--silver)"/>
    <path class="base-band" d="M0 360 C180 360 300 340 380 330 L1160 318 V400 Q1160 440 1120 440 H40 Q0 440 0 400 Z" fill="var(--black)"/>
    <rect x="530" y="50" width="70" height="70" fill="var(--ink)"/>
    <text class="brand-name" x="680" y="168" font-size="50" fill="var(--ink)" text-anchor="middle">KORVELT</text>
    <text class="web" x="585" y="222" font-size="22" fill="var(--ink)" text-anchor="middle">www.KORVELT.CO.UK</text>
    <text class="phone" x="585" y="275" font-size="46" fill="var(--cream)" text-anchor="middle">08001 742 905</text>
  </svg>

  <!-- Passenger side panel -->
  <svg class="panel side-right" width="1160" height="440" viewBox="0 0 1160 440">
    <g transform="translate(1160,0) scale(-1,1)">
      <rect class="wrap-base" x="0" y="0" width="1160" height="440" rx="40" fill="url(#bronzeSide)"/>
      <path class="building-photo" role="img" aria-label="Photo of a modern brick apartment building" d="M880 0 H1120 Q1160 0 1160 40 V300 L820 300 C860 210 865 90 880 0 Z" fill="url(#buildingTone)"/>
      <path class="accent-swoosh" d="M880 0 C865 90 860 210 820 300 L1160 300 V318 L380 330 C560 300 740 320 800 290 C840 200 850 90 865 0 Z" fill="var(--silver)"/>
      <path class="base-band" d="M0 360 C180 360 300 340 380 330 L1160 318 V400 Q1160 440 1120 440 H40 Q0 440 0 400 Z" fill="var(--black)"/>
    </g>
    <rect x="420" y="40" width="70" height="70" fill="var(--ink)"/>
    <text class="brand-name" x="500" y="165" font-size="50" fill="var(--ink)" text-anchor="middle">KORVELT</text>
    <text class="web" x="580" y="235" font-size="22" fill="var(--ink)" text-anchor="middle">www.KORVELT.CO.UK</text>
    <text class="phone" x="595" y="288" font-size="46" fill="var(--cream)" text-anchor="middle">08001 742 905</text>
  </svg>

  <!-- Rear doors panel -->
  <svg class="panel rear" width="700" height="600" viewBox="0 0 700 600">
    <rect class="wrap-base" x="0" y="0" width="700" height="600" rx="50" fill="var(--black)"/>
    <rect class="rear-window-frame" x="90" y="40" width="520" height="190" rx="60" fill="none" stroke="#2a2a2a" stroke-width="4"/>
    <text class="phone" x="340" y="110" font-size="56" fill="var(--white)" text-anchor="middle">08001 742 905</text>
    <rect x="120" y="150" width="52" height="52" fill="var(--cream)"/>
    <text class="brand-name" x="385" y="197" font-size="48" fill="var(--cream)" text-anchor="middle">KORVELT</text>
    <text class="web" x="380" y="262" font-size="26" fill="var(--white)" text-anchor="middle">www.KORVELT.CO.UK</text>
    <g class="service-list" fill="var(--white)">
      <circle cx="125" cy="362" r="5"/><text class="service" x="138" y="370" font-size="22">New Builds</text>
      <circle cx="125" cy="388" r="5"/><text class="service" x="138" y="396" font-size="22">Basement Works</text>
      <circle cx="125" cy="414" r="5"/><text class="service" x="138" y="422" font-size="22">Piling Works</text>
      <circle cx="125" cy="440" r="5"/><text class="service" x="138" y="448" font-size="22">Demolition</text>
      <circle cx="395" cy="362" r="5"/><text class="service" x="408" y="370" font-size="22">Engineering</text>
      <circle cx="395" cy="388" r="5"/><text class="service" x="408" y="396" font-size="22">RC Frame Works</text>
      <circle cx="395" cy="414" r="5"/><text class="service" x="408" y="422" font-size="22">Loft Conversions</text>
      <circle cx="395" cy="440" r="5"/><text class="service" x="408" y="448" font-size="22">Refurbishment</text>
    </g>
  </svg>

  <!-- Front bonnet panel -->
  <svg class="panel front" width="820" height="460" viewBox="0 0 820 460">
    <defs>
      <linearGradient id="bronzeFront" x1="0" y1="0" x2="0" y2="1">
        <stop offset="0" stop-color="var(--bronze-light)"/>
        <stop offset="0.6" stop-color="var(--bronze)"/>
        <stop offset="1" stop-color="var(--bronze-dark)"/>
      </linearGradient>
    </defs>
    <rect class="wrap-base" x="0" y="0" width="820" height="460" rx="60" fill="url(#bronzeFront)"/>
    <path class="accent-swoosh" d="M125 0 H695 C665 90 600 160 560 210 H260 C220 160 155 90 125 0 Z" fill="var(--silver)"/>
    <path class="front-band" d="M160 0 H660 C640 90 590 160 550 210 H270 C230 160 180 90 160 0 Z" fill="var(--black)"/>
    <rect x="240" y="65" width="50" height="50" fill="var(--cream)"/>
    <text class="brand-name" x="440" y="108" font-size="42" fill="var(--cream)" text-anchor="middle">KORVELT</text>
  </svg>
</main>
</body>
</html>
```